Business Card Design Project

I am looking for a double sided business card design that is bold on one side with creative use of the logo, but clean and professional looking on the other side with the contact information provided.

Target Market(s)

My target market is recruitment agents, senior managers of multinational companies. The target segments are finance and I.T.

Industry/Entity Type

Business

Requirements
Must have
• Double sided. Use provided logo.

Information to include, but use your creativity for the tags (example):
Name (Marcus Feldane)
Position (Director)
Mobile (+44 7XXXXXXXXX)
Phone (+44 20XXXXXXXX)
Email (marcus@wendlebymarsh.com)
Website (www.wendlebymarsh.com)

```html
<!DOCTYPE html>
<html lang="en">
<head>
<meta charset="utf-8">
<title>Wendleby Marsh Consulting – Business Card</title>
<link rel="stylesheet" href="https://fonts.googleapis.com/css2?family=Exo+2:wght@400;600&display=swap">
<style>
  :root {
    --stage: #3a3a3a;
    --card-white: #ffffff;
    --brand-blue: #1a74c4;
    --brand-blue-deep: #0f5fa8;
    --brand-lime: #d4dc12;
    --text-blue: #2b84d0;
  }
  * { margin: 0; padding: 0; box-sizing: border-box; }
  html, body {
    width: 1200px;
    height: 900px;
    overflow: hidden;
    background: var(--stage);
    font-family: "Exo 2", sans-serif;
  }
  .stage {
    width: 1200px;
    height: 900px;
    display: flex;
    flex-direction: column;
    align-items: center;
    justify-content: center;
    gap: 40px;
  }
  .card {
    position: relative;
    width: 700px;
    height: 400px;
    border-radius: 4px;
    overflow: hidden;
    box-shadow: 0 10px 30px rgba(0,0,0,0.45);
  }

  /* Back side: bold brand face */
  .card-back {
    background: linear-gradient(135deg, var(--brand-blue) 0%, var(--brand-blue-deep) 100%);
    display: flex;
    align-items: center;
    justify-content: center;
  }
  .brand-lockup {
    display: flex;
    align-items: center;
    gap: 22px;
  }
  .brand-dot {
    width: 70px;
    height: 70px;
    border-radius: 50%;
    background: var(--brand-lime);
  }
  .brand-name {
    color: var(--card-white);
    font-weight: 600;
    font-size: 34px;
    line-height: 1.15;
    letter-spacing: 1px;
    text-transform: uppercase;
  }

  /* Front side: contact face */
  .card-front { background: var(--card-white); }
  .front-curves {
    position: absolute;
    inset: 0;
  }
  .contact {
    position: absolute;
    left: 250px;
    top: 92px;
    color: var(--text-blue);
  }
  .contact-name {
    font-weight: 600;
    font-size: 38px;
    line-height: 1;
  }
  .contact-role {
    font-size: 17px;
    font-weight: 400;
    letter-spacing: 0.5px;
    margin-top: 4px;
    text-transform: uppercase;
  }
  .contact-list {
    list-style: none;
    margin-top: 26px;
    font-size: 19px;
    line-height: 1.3;
  }
</style>
</head>
<body>
<main class="stage">
  <section class="card card-back" aria-label="Business card back">
    <div class="brand-lockup">
      <span class="brand-dot"></span>
      <p class="brand-name">Wendleby Marsh<br>Consulting Limited</p>
    </div>
  </section>

  <section class="card card-front" aria-label="Business card front">
    <svg class="front-curves" viewBox="0 0 700 400" width="700" height="400" aria-hidden="true">
      <path fill="var(--brand-blue)" d="M470 0 L700 0 L700 400 L600 400 C700 300 690 100 470 0 Z"/>
      <path fill="var(--brand-lime)" d="M520 30 C650 120 650 300 500 400 L565 400 C680 300 670 110 520 30 Z"/>
    </svg>
    <div class="contact">
      <h1 class="contact-name">Marcus Feldane</h1>
      <p class="contact-role">Director</p>
      <ul class="contact-list">
        <li>m: 0413 118 902</li>
        <li>p: 02 9655 3100</li>
        <li>e: marcus@wendlebymarsh.com</li>
        <li>w: www.wendlebymarsh.com</li>
      </ul>
    </div>
  </section>
</main>
</body>
</html>
```